Private Medical Clinic needs a letterhead design

Letterhead that can be edited. Letter head is needed for printing official doctor's notes, referrals, etc in a medical clinic. The letterhead should use the attached logos

```html
<!DOCTYPE html>
<html lang="en">
<head>
<meta charset="utf-8">
<title>Willow Creek Family Medicine – Letterhead</title>
<link rel="stylesheet" href="https://fonts.googleapis.com/css2?family=EB+Garamond:wght@400&family=Source+Sans+3:wght@400;600&display=swap">
<style>
  :root {
    --backdrop: #a4a5a4;
    --paper: #ffffff;
    --forest: #4a5e3b;
    --ink: #2b2b2b;
    --icon: #7a7a7a;
    --gold-edge: #c8953f;
    --gold-mid: #efc766;
    --gold-light: #f9ec98;
    --mist: #fff8d6;
  }
  * { box-sizing: border-box; margin: 0; padding: 0; }
  html, body { width: 895px; height: 1200px; overflow: hidden; }
  body { background: var(--backdrop); position: relative; }

  .letterhead {
    position: absolute; left: 78px; top: 77px;
    width: 739px; height: 1045px;
    background: var(--paper);
    box-shadow: 0 2px 8px rgba(0,0,0,.25);
    overflow: hidden;
  }

  .brand { position: absolute; left: 32px; top: 66px; }
  .brand__name {
    font-family: "EB Garamond", serif; font-weight: 400;
    color: var(--forest); font-size: 52px; line-height: 1;
    letter-spacing: -0.5px;
  }
  .brand__sub {
    font-family: "EB Garamond", serif; font-weight: 400;
    color: var(--forest); font-size: 13px; letter-spacing: 2.2px;
    margin-top: 4px;
  }

  .tagline {
    position: absolute; left: 35px; top: 170px; width: 263px;
    font-family: "Source Sans 3", sans-serif; font-weight: 400;
    color: var(--forest); font-size: 18.5px; letter-spacing: 0.1px;
    padding-bottom: 3px; border-bottom: 1px solid var(--forest);
    white-space: nowrap;
  }
  .physician {
    position: absolute; left: 36px; top: 202px;
    font-family: "Source Sans 3", sans-serif; font-weight: 600;
    color: var(--forest); font-size: 19px;
  }

  .contact { position: absolute; left: 518px; top: 31px; list-style: none; }
  .contact__item {
    display: flex; align-items: center; height: 22.4px;
    font-family: "Source Sans 3", sans-serif; font-size: 10.8px; color: var(--ink);
  }
  .contact__icon {
    width: 12px; height: 12px; margin-right: 7px; flex: none;
    fill: none; stroke: var(--icon); stroke-width: 1;
  }

  .watermark-art {
    position: absolute; left: 40px; top: 515px; width: 355px; height: 460px;
    background: radial-gradient(ellipse 55% 40% at 30% 25%, var(--mist) 0%, rgba(255,248,214,.5) 55%, rgba(255,255,255,0) 100%),
                radial-gradient(ellipse 35% 30% at 35% 80%, rgba(255,248,214,.7) 0%, rgba(255,255,255,0) 100%);
  }

  .footer-band { position: absolute; left: 0; bottom: 0; width: 739px; height: 74px; display: block; }
</style>
</head>
<body>
  <main class="letterhead">
    <div class="brand">
      <div class="brand__name">Willow Creek</div>
      <div class="brand__sub">FAMILY MEDICINE</div>
    </div>

    <div class="tagline">HEALING THE WHOLE PERSON</div>
    <div class="physician">Dr. Martin Ellsworth</div>

    <ul class="contact">
      <li class="contact__item">
        <svg class="contact__icon" viewBox="0 0 12 12"><rect x="1" y="2.5" width="10" height="7"/><path d="M1 2.5l5 4 5-4"/></svg>
        hello@willowcreekclinic.com
      </li>
      <li class="contact__item">
        <svg class="contact__icon" viewBox="0 0 12 12"><rect x="3" y="1" width="6" height="3"/><rect x="1" y="4" width="10" height="5"/><rect x="3" y="7" width="6" height="4"/></svg>
        01632 960 4417
      </li>
      <li class="contact__item">
        <svg class="contact__icon" viewBox="0 0 12 12"><rect x="3" y="0.5" width="6" height="11" rx="1"/><path d="M5 9.5h2"/></svg>
        +01 5550148823
      </li>
      <li class="contact__item">
        <svg class="contact__icon" viewBox="0 0 12 12"><path d="M1 5c0-2 2-3 5-3s5 1 5 3l-2 .5-.5-1.5h-5L3 5.5z"/><rect x="2.5" y="6" width="7" height="4" rx="1"/></svg>
        020 7946 018233
      </li>
      <li class="contact__item">
        <svg class="contact__icon" viewBox="0 0 12 12"><circle cx="6" cy="6" r="5"/><ellipse cx="6" cy="6" rx="2.2" ry="5"/><path d="M1 6h10"/></svg>
        willowcreekclinic.com
      </li>
      <li class="contact__item">
        <svg class="contact__icon" viewBox="0 0 12 12"><path d="M6 11.5S2 7 2 4.5a4 4 0 0 1 8 0C10 7 6 11.5 6 11.5z"/><circle cx="6" cy="4.5" r="1.4"/></svg>
        #27, Harbor Point, Suite 3B10, USA
      </li>
    </ul>

    <div class="watermark-art" role="img" aria-label="Faint pale-yellow botanical watermark of the clinic emblem"></div>

    <svg class="footer-band" viewBox="0 0 739 74" preserveAspectRatio="none" aria-hidden="true">
      <defs>
        <linearGradient id="gold" x1="0" x2="1" y1="0" y2="0">
          <stop offset="0" stop-color="var(--gold-edge)"/>
          <stop offset="0.2" stop-color="var(--gold-mid)"/>
          <stop offset="0.6" stop-color="var(--gold-light)"/>
          <stop offset="0.85" stop-color="var(--gold-mid)"/>
          <stop offset="1" stop-color="var(--gold-edge)"/>
        </linearGradient>
      </defs>
      <path d="M0 46 C150 10 300 0 380 0 C480 0 600 14 739 47 L739 74 L0 74 Z" fill="var(--forest)"/>
      <path d="M0 48 C150 20 300 12 380 12 C480 12 600 24 739 48 L739 74 L0 74 Z" fill="url(#gold)"/>
    </svg>
  </main>
</body>
</html>
```